Ice Cream Product Packaging - Bucket and Lid

We need some high quality packaging designed for a client who manufactures and sells 'healthy' Ice Cream (low calories, high protein etc).
The logo needs to be designed also which is the main image of the packaging.
Prefer lower case for main fonts. needs to look elegant, naughty and high end.
There are 2 flavours at this stage - chocolate and vanilla.
Target market is for adults - 18-40, fitness, gym etc.

There are 2 sizes but let's just get the largest one sorted first?

Title: "lumé" (means 'kiss' in French) - they want an image of some pronounced red lips behind the name. The red lips will be their main brand identity/logo.. With some chocolate dripping out of the side. (brown for the chocolate flavour and a cream colour for the vanilla flavour). Maybe a faded image of an attactive womans face - mainly the lips and chin (if chin is necessary?!) - the text "Ice Creamery" can be in a small font underneath

Subtitle: Can go above (or below) main title: "naughty & healthy" followed on the next line by: "Low Calories + High Protein" (they are thinking about spelling 'naughty' incorrectly - like "nauty".. I'm not sure about this though..what do you think?!) This text can be in gold or silver perhaps and a handwriting font to give it that high end look? Up to you.

Background - whatever you think.. some sort of nice textured background perhaps? brown shades for the chocolate flavour, creamy/yellowy shades for the vanilla flavour. Can we also have some ice cream 'dripping' from the top.

There will be a section of 6 lips icons that will say: Gluten Free, High Protein, Low Calories, Lactose Free, No Added Sugar, Digestive Enzyme. These icons can go down the side of the bucket.

Colours: Red, black, brown (for choc), cream (for vanilla), gold and/or silver, white or cream etc etc.
Bucket for chocolate will be black so there is a black lip at the top (tamper proof seal). Bucket for Vanilla is white so will be white at the top - tamper proof seal. incorporate those colurs.

We also need some room for ingredients text, barcode and some company info.

Please see the files attachedfor a rough version. Doesn't need to be exactly the same but something similar would be fantastic.

Also attached are the 2 ice cream bucket sizes, their dimensions and the Lid size.
Lid will just be a copy of the main image on the bucket.

Target Market(s)

adults, 18-40, fitness, healthy, gym, foodies

Font styles to use
Sans Serif
Script

Colors
ec1f27
f04a50
fff3d1
ffffff
1b1b1b

Requirements
Must have
• Elegant look, high end, healthy ice cream, red lips... see description for more detailed info
Nice to have
• see description for more detailed info
Should not have

```html
<!DOCTYPE html>
<html lang="en">
<head>
<meta charset="utf-8">
<title>lumé ice cream — tub labels</title>
<link rel="stylesheet" href="https://fonts.googleapis.com/css2?family=Kalam:wght@400;700&display=swap">
<style>
  :root {
    --stage: #ecebe8;
    --choc: #8a5d45;
    --choc-soft: #b98b70;
    --choc-dark: #3b2418;
    --cream: #f3ece0;
    --vanilla: #efe2c2;
    --vanilla-line: #d7b978;
    --brand-blue: #4fa7d9;
    --lip-red: #d8262b;
    --ink-light: #fbf6ee;
  }
  * { box-sizing: border-box; margin: 0; padding: 0; }
  html, body { width: 1200px; height: 1200px; overflow: hidden; }
  body {
    background: var(--stage);
    font-family: "Kalam", cursive;
    position: relative;
  }
  .label {
    position: absolute;
    overflow: hidden;
    border-radius: 6px;
    box-shadow: 0 2px 10px rgba(0,0,0,.12);
  }
  .label--front { width: 540px; height: 560px; top: 50px; }
  .label--choc { left: 50px; background: var(--cream); }
  .label--vanilla { left: 610px; background: var(--cream); }
  .label--back { left: 50px; top: 650px; width: 1100px; height: 500px; background: var(--cream); }

  .band { position: absolute; left: 0; right: 0; }
  .band--top { top: 0; height: 110px; }
  .band--bottom { bottom: 0; height: 130px; }
  .label--choc .band, .label--back .band { background: var(--choc); }
  .label--vanilla .band { background: var(--vanilla); }

  .tagline {
    position: absolute; top: 34px; left: 110px;
    font-weight: 700; font-size: 38px; color: var(--brand-blue);
  }
  .drip {
    position: absolute; top: 0; left: 20px; width: 60px; height: 190px;
    border-radius: 0 0 30px 30px;
  }
  .label--choc .drip { background: var(--choc-dark); }
  .label--vanilla .drip { background: var(--vanilla-line); opacity: .6; }

  .arch {
    position: absolute; left: 120px; bottom: 130px; width: 300px; height: 150px;
    border-radius: 150px 150px 0 0;
  }
  .label--choc .arch { background: var(--choc); }
  .label--vanilla .arch { background: var(--vanilla); }

  .wordmark {
    position: absolute; top: 150px; left: 0; right: 0; text-align: center;
    font-weight: 700; font-size: 150px; line-height: 1; color: var(--brand-blue);
  }
  .lips {
    position: absolute; left: 190px; bottom: 150px; width: 160px; height: 100px;
    border-radius: 50%; background: var(--lip-red);
  }
  .product-word {
    position: absolute; bottom: 145px; font-weight: 700; font-size: 44px;
  }
  .label--choc .product-word { color: var(--choc-dark); }
  .label--vanilla .product-word { color: var(--vanilla-line); }
  .product-word--left { left: 40px; }
  .product-word--right { right: 40px; }

  .benefits {
    position: absolute; left: 0; right: 0; bottom: 0; height: 130px;
    display: flex; justify-content: space-around; align-items: center; padding: 0 30px;
  }
  .benefit { display: flex; flex-direction: column; align-items: center; gap: 6px; font-size: 20px; font-weight: 700; }
  .label--choc .benefit, .label--back .benefit { color: var(--ink-light); }
  .label--vanilla .benefit { color: var(--vanilla-line); }
  .benefit svg { width: 52px; height: 52px; }

  .why-panel {
    position: absolute; top: 110px; bottom: 130px; left: 60px; width: 480px;
    background: var(--choc-soft); color: var(--ink-light);
    text-align: center; font-size: 40px; line-height: 1.2; padding-top: 30px;
  }
  .ingredients-panel {
    position: absolute; top: 110px; bottom: 130px; left: 540px; right: 60px;
    background: var(--cream); color: var(--choc); padding: 30px 40px;
  }
  .ingredients-panel h2 { font-size: 42px; font-weight: 700; }
  .keep-frozen { position: absolute; bottom: 20px; left: 40px; font-size: 28px; font-weight: 700; }
</style>
</head>
<body>

<section class="label label--front label--choc" aria-label="Chocolate tub front label">
  <div class="band band--top"></div>
  <div class="drip" role="img" aria-label="Chocolate dripping from the rim"></div>
  <p class="tagline">naughty but healthy</p>
  <div class="arch"></div>
  <h1 class="wordmark">lumé</h1>
  <div class="lips" role="img" aria-label="Glossy red lips illustration"></div>
  <span class="product-word product-word--left">ice</span>
  <span class="product-word product-word--right">cream</span>
  <div class="band band--bottom"></div>
  <ul class="benefits">
    <li class="benefit">High Protein
      <svg viewBox="0 0 52 52" fill="none" stroke="currentColor" stroke-width="3"><circle cx="26" cy="26" r="23"/><path d="M14 26h24M14 20v12M18 18v16M38 20v12M34 18v16"/></svg></li>
    <li class="benefit">Digestive Enzyme
      <svg viewBox="0 0 52 52" fill="none" stroke="currentColor" stroke-width="3"><circle cx="26" cy="26" r="23"/><circle cx="20" cy="22" r="6"/><circle cx="32" cy="22" r="6"/><circle cx="26" cy="32" r="6"/></svg></li>
    <li class="benefit">Low Calories
      <svg viewBox="0 0 52 52" fill="none" stroke="currentColor" stroke-width="3"><circle cx="26" cy="26" r="23"/><path d="M26 13c6 8 10 12 10 19a10 10 0 0 1-20 0c0-5 3-8 5-10 0 4 2 6 4 6 0-5-2-9 1-15z"/></svg></li>
  </ul>
</section>

<section class="label label--front label--vanilla" aria-label="Vanilla tub front label">
  <div class="band band--top"></div>
  <div class="drip" role="img" aria-label="Vanilla dripping from the rim"></div>
  <p class="tagline">naughty but healthy</p>
  <div class="arch"></div>
  <h1 class="wordmark">lumé</h1>
  <div class="lips" role="img" aria-label="Glossy red lips illustration"></div>
  <span class="product-word product-word--left">ice</span>
  <span class="product-word product-word--right">cream</span>
  <div class="band band--bottom"></div>
  <ul class="benefits">
    <li class="benefit">High Protein
      <svg viewBox="0 0 52 52" fill="none" stroke="currentColor" stroke-width="3"><circle cx="26" cy="26" r="23"/><path d="M14 26h24M14 20v12M18 18v16M38 20v12M34 18v16"/></svg></li>
    <li class="benefit">Digestive Enzyme
      <svg viewBox="0 0 52 52" fill="none" stroke="currentColor" stroke-width="3"><circle cx="26" cy="26" r="23"/><circle cx="20" cy="22" r="6"/><circle cx="32" cy="22" r="6"/><circle cx="26" cy="32" r="6"/></svg></li>
    <li class="benefit">Low Calories
      <svg viewBox="0 0 52 52" fill="none" stroke="currentColor" stroke-width="3"><circle cx="26" cy="26" r="23"/><path d="M26 13c6 8 10 12 10 19a10 10 0 0 1-20 0c0-5 3-8 5-10 0 4 2 6 4 6 0-5-2-9 1-15z"/></svg></li>
  </ul>
</section>

<section class="label label--back" aria-label="Chocolate tub back label">
  <div class="band band--top"></div>
  <div class="why-panel">Why choose<br>lumé?</div>
  <div class="ingredients-panel">
    <h2>Ingredients</h2>
    <p class="keep-frozen">Keep Frozen</p>
  </div>
  <div class="band band--bottom"></div>
  <ul class="benefits">
    <li class="benefit">Collagen
      <svg viewBox="0 0 52 52" fill="none" stroke="currentColor" stroke-width="3"><circle cx="26" cy="26" r="23"/><path d="M33 19a10 10 0 1 0 0 14"/></svg></li>
    <li class="benefit">Gluten Free
      <svg viewBox="0 0 52 52" fill="none" stroke="currentColor" stroke-width="3"><circle cx="26" cy="26" r="23"/><path d="M26 14v26M20 20l6 6 6-6M20 28l6 6 6-6M12 40l28-28"/></svg></li>
    <li class="benefit">Lactose Free
      <svg viewBox="0 0 52 52" fill="none" stroke="currentColor" stroke-width="3"><circle cx="26" cy="26" r="23"/><path d="M21 14h10v6l4 6v14H17V26l4-6zM12 40l28-28"/></svg></li>
    <li class="benefit">No Added Sugar
      <svg viewBox="0 0 52 52" fill="none" stroke="currentColor" stroke-width="3"><circle cx="26" cy="26" r="23"/><path d="M16 22l10-6 10 6v12l-10 6-10-6zM16 22l10 6 10-6M26 28v12"/></svg></li>
  </ul>
</section>

</body>
</html>
```